Web site for Tree Removal Company

What we are looking for:
-------------------------------
Looking for a wordpress web site, you can provide your own template or we can supply you with one (http://quorvel.plindatheme.net).

What we do
---------------
To see what we do please go to google Australia and google "Tree removal Sydney" or "Tree Removal Melbourne".

Web site requirements
-----------------------------
We prefer you to use our template as it has all our requirements in already.
- Responsive.
- Based on Wordpress.
- Full complaint and compatible with plugs.

Look, Feel and Appearance
------------------------------------
Please use the logo (see attached), for colour scheme, look and feel of the web site.

Thank you for your time and effort!

Target Market(s)

Tree Removal for Residential Homes

Industry/Entity Type

It Company

Number of Pages Required

4 page

Font styles to use
Serif
Sans Serif

Requirements
Must have
• Wordpress
Nice to have
• Original artwork, images and text
Should not have
• non related images or wording

```html
<!DOCTYPE html>
<html lang="en">
<head>
<meta charset="utf-8">
<title>Leafwright – Tree Services</title>
<link rel="stylesheet" href="https://fonts.googleapis.com/css2?family=Open+Sans:ital,wght@0,300;0,400;0,600;0,700;1,300&display=swap">
<style>
:root{
  --black:#000;
  --footer:#161616;
  --bar:#0b0b0b;
  --white:#fff;
  --text:#444;
  --muted:#555;
  --grey-band:#ebebeb;
  --green:#2f6b5c;
  --green-dark:#1f4a40;
  --field:#3a3a3a;
}
*{margin:0;padding:0;box-sizing:border-box}
html,body{width:806px;height:1200px;overflow:hidden;background:var(--white)}
body{position:relative;font-family:"Open Sans",sans-serif;color:var(--text)}
.site-header{position:absolute;top:0;left:0;width:806px;height:64px;background:var(--black)}
.brand{position:absolute;left:110px;top:18px;display:flex;align-items:center;gap:6px;color:var(--white);font-size:13px;font-weight:600;letter-spacing:1px}
.brand-mark{width:12px;height:12px;border-radius:50%;background:#5fa57f}
.main-nav{position:absolute;top:23px;left:0;width:806px}
.main-nav a{position:absolute;color:var(--white);text-decoration:none;font-size:12px}
.hero{position:absolute;top:64px;left:0;width:806px;height:303px;background:linear-gradient(110deg,#6d7c52 0%,#8b8677 30%,#5a5650 55%,#7f7362 75%,#a8502e 100%)}
.hero-panel{position:absolute;top:65px;left:0;width:806px;height:173px;background:rgba(20,20,20,.82);text-align:center;color:var(--white)}
.hero-title{font-size:52px;font-weight:700;letter-spacing:1px;margin-top:22px;line-height:1.1}
.hero-text{font-size:8.5px;font-weight:300;line-height:18px;width:570px;margin:24px auto 0}
.slider-dots{position:absolute;top:291px;left:388px;display:flex;gap:4px}
.slider-dots span{width:6px;height:6px;border-radius:50%;background:rgba(60,60,60,.6)}
.slider-dots span.active{background:#111}
.services{position:absolute;top:416px;left:108px;width:592px;display:flex;gap:14px}
.service{width:138px;text-align:center}
.service-photo{height:140px}
.service h3{font-size:9px;font-weight:600;color:#333;margin-top:18px;letter-spacing:.3px}
.service p{font-size:7.5px;line-height:18px;color:var(--muted);margin-top:10px}
.cta{position:absolute;top:719px;left:0;width:806px;height:124px;background:linear-gradient(90deg,#4f5a34 0%,#8a6a48 30%,#b48a65 55%,#7b7047 80%,#5c6a3a 100%)}
.cta h2{position:absolute;left:131px;top:48px;color:var(--white);font-size:20px;font-weight:700;letter-spacing:.4px;text-shadow:0 1px 3px rgba(0,0,0,.5)}
.cta-button{position:absolute;left:549px;top:46px;width:137px;height:34px;background:var(--green);border-bottom:3px solid var(--green-dark);color:var(--white);font-size:14px;font-weight:700;text-align:center;line-height:32px;border-radius:2px}
.welcome{position:absolute;top:843px;left:0;width:806px;height:154px;background:var(--grey-band);text-align:center}
.welcome h2{font-size:15px;font-weight:600;color:#3a3a3a;margin-top:27px;letter-spacing:.4px}
.welcome p{width:580px;margin:17px auto 0;font-size:8.5px;line-height:18px;font-weight:300;color:#333}
.site-footer{position:absolute;top:997px;left:0;width:806px;height:174px;background:var(--footer);color:var(--white)}
.footer-col{position:absolute;top:24px;width:140px}
.footer-col h4{font-size:9px;font-weight:600;letter-spacing:.2px}
.footer-col p{margin-top:40px;font-size:7.5px;line-height:18px;font-weight:300;padding-left:2px}
.footer-col p.quote{font-style:italic}
.footer-col .author{font-size:8.5px;font-weight:600;line-height:18px;padding-left:2px}
.newsletter{margin-top:40px;width:137px;height:20px;background:var(--field);display:flex;justify-content:space-between;align-items:center;padding-left:8px;font-size:7px;font-style:italic;color:#ccc}
.newsletter b{width:20px;height:18px;margin-right:1px;background:#000;color:var(--white);font-style:normal;font-size:9px;font-weight:700;line-height:18px;text-align:center}
.bottom-bar{position:absolute;top:1171px;left:0;width:806px;height:29px;background:var(--bar);color:#aaa;font-size:7.5px;text-align:center;line-height:29px}
</style>
</head>
<body>
<header class="site-header">
  <div class="brand"><span class="brand-mark"></span>Leafwright</div>
  <nav class="main-nav">
    <a style="left:365px">Home</a>
    <a style="left:440px">Tree Services</a>
    <a style="left:550px">Safety FAQs</a>
    <a style="left:654px">Contact</a>
  </nav>
</header>

<section class="hero" role="img" aria-label="Chainsaw cutting through a felled log on grass">
  <div class="hero-panel">
    <h1 class="hero-title">PROFESSIONAL</h1>
    <p class="hero-text">Lorem Ipsum is simply dummy text of the printing and typesetting industry. Lorem Ipsum has been the industry's standard dummy text ever since the 1500s, when an unknown printer took a galley of type and scrambled it to make a type specimen book.</p>
  </div>
  <div class="slider-dots"><span></span><span class="active"></span><span></span></div>
</section>

<section class="services">
  <article class="service">
    <div class="service-photo" role="img" aria-label="Large leafy tree standing in a field" style="background:linear-gradient(180deg,#cfe2ee 0%,#4f8a2e 35%,#3c6e23 70%,#b8ab95 100%)"></div>
    <h3>IDENTIFY ANY TREES</h3>
    <p>Information like species, whether it is dead or alive, and the height, will be required in any applications required by your local council....</p>
  </article>
  <article class="service">
    <div class="service-photo" role="img" aria-label="Arborist carrying a log and a chainsaw" style="background:linear-gradient(180deg,#e3e3e3 0%,#c9c9c9 100%)"></div>
    <h3>CONTACT A PROFESSIONAL</h3>
    <p>You should perform some due diligence on the company before you use them. Check that they have Arbori-culture....</p>
  </article>
  <article class="service">
    <div class="service-photo" role="img" aria-label="Chainsaw cutting into a tree trunk" style="background:linear-gradient(90deg,#3c6ea0 0%,#6b8fb0 30%,#8a5a3e 55%,#6a4530 75%,#6f8f55 100%)"></div>
    <h3>REMOVE THE TREE</h3>
    <p>Once qualified arborist has come, assessed the working conditions, pre-pared a quote, and you have now accepted....</p>
  </article>
  <article class="service">
    <div class="service-photo" role="img" aria-label="Worker in a hard hat clearing branches in a garden" style="background:linear-gradient(180deg,#6e8b3d 0%,#8fae5a 45%,#5d7a33 100%)"></div>
    <h3>BRANCHES</h3>
    <p>Once qualified arborist has come, assessed the working conditions, pre-pared a quote, and you have now accepted....</p>
  </article>
</section>

<section class="cta" role="img" aria-label="Blurred cut logs lying in a forest">
  <h2>CONTACT OUR TEAM FOR ANY HELP !</h2>
  <div class="cta-button">HELP !</div>
</section>

<section class="welcome">
  <h2>WELCOME TO OUR SITE</h2>
  <p>Lorem Ipsum is simply dummy text of the printing and typesetting industry. Lorem Ipsum has been the industry's standard dummy text ever since the 1500s, when an unknown printer took a galley of type and scrambled it to make a type specimen book. It has survived not only five centuries, but also the leap into electronic typesetting, remaining essentially unchanged. It was popularised...</p>
</section>

<footer class="site-footer">
  <div class="footer-col" style="left:108px">
    <h4>CONTACT US</h4>
    <p>Address Line1, Address Line2,<br>city zip-code,<br>(+9) - 412 - 7730 - 615<br>info@leafwright.com</p>
  </div>
  <div class="footer-col" style="left:259px">
    <h4>TESTIMONIAL</h4>
    <p class="quote">Lorem Ipsum is simply dummy text of the printing and typesetting industry. Lorem Ipsum has been the industry's standard dummy....</p>
    <div class="author">- Maren</div>
  </div>
  <div class="footer-col" style="left:410px">
    <h4>NEWSLETTER</h4>
    <div class="newsletter">E-Mail<b>GO</b></div>
  </div>
  <div class="footer-col" style="left:562px">
    <h4>ABOUT US</h4>
    <p>Lorem Ipsum is simply dummy text of the printing and typesetting industry. Lorem Ipsum has been the industry's standard dummy....</p>
  </div>
</footer>
<div class="bottom-bar">©2015 - leafwright.com</div>
</body>
</html>
```